Asia based real estate financing firm needs and AWESOME design for a biz card -Harbor Lending Circle

Looking for a stylish, & corporate-looking business card for a real estate financing brokerage firm in Asia, offering global mortgage loans. I uploaded our current logos. We would like to add a splash of color (perhaps the house icon) or any other suggestions are open. For the winning designer, we have a lot of work! Thanks and best of luck!

Target Market(s)

Real estate investors globally. We want to look more like a BANK and NOT a real estate company. Please don't play up on a "house" design.

Industry/Entity Type

Banking

Contact Information for Business Card

Harbor Lending Circle
Peter Wilks
Co-Founder | Partner

14 Cassia Lane, Suite 310
Singapore 047219
www.hlc-example.asia
peterwilks@hlc-example.asia
+65 555-0142
WeChat: peterwilks

Colors

Designer to choose colors to be used in the design.

Requirements
Must have
• Must have the standard business requirements for a card; name, address, email, etc
• Can be horizontal or vertical.
Nice to have
• It would be great to see some sort of variation to the logo with a pop of color. Red is good as we're in Asia, however, other options work as well.
• Our tag line is - Lending Across Shores. It doesn't have to be on the card but might be nice.
• I'd like to start seeing our tagline within the cards as well. - Lending Across Shores.
• Also, please add our location. The location for this card is Singapore so perhaps it can be highlighted or emphasised in some way.
• Singapore | Hong Kong | Shanghai | Manila
• As we will soon open an office in Shanghai, having an option for both languages would be great.
Should not have
• I'm exceited and open to your creativity ... knock it out of the park!

```html
<!DOCTYPE html>
<html lang="en">
<head>
<meta charset="utf-8">
<title>Harbor Lending Circle – Business Card</title>
<link rel="stylesheet" href="https://fonts.googleapis.com/css2?family=Cormorant+Garamond:wght@500&family=Nunito+Sans:wght@300;400;700&display=swap">
<style>
  :root {
    --page: #e9e4dc;
    --card: #1b181a;
    --panel: #2b1e20;
    --ink: #f3f1ee;
    --ink-soft: #cfcac6;
    --shadow: rgba(0, 0, 0, 0.22);
  }
  * { box-sizing: border-box; margin: 0; padding: 0; }
  html, body {
    width: 1200px;
    height: 795px;
    overflow: hidden;
    background: var(--page);
  }
  .stage {
    width: 1200px;
    height: 795px;
    display: flex;
    align-items: center;
    justify-content: center;
    gap: 80px;
  }
  .card {
    width: 340px;
    height: 580px;
    background: var(--card);
    color: var(--ink);
    position: relative;
    box-shadow: 0 10px 26px var(--shadow);
  }
  .brand-name {
    font-family: "Cormorant Garamond", serif;
    font-weight: 500;
    color: var(--ink);
    letter-spacing: 0.05em;
    white-space: nowrap;
  }

  /* Front */
  .card--front .brand-name {
    position: absolute;
    left: 0;
    right: 0;
    top: 250px;
    text-align: center;
    font-size: 28px;
  }

  /* Back */
  .card--back .brand-name {
    position: absolute;
    left: 0;
    right: 0;
    top: 96px;
    text-align: center;
    font-size: 20px;
  }
  .holder {
    position: absolute;
    left: 0;
    right: 0;
    top: 170px;
    text-align: center;
    font-family: "Nunito Sans", sans-serif;
  }
  .holder-name {
    font-weight: 700;
    font-size: 18px;
    letter-spacing: 0.05em;
  }
  .holder-title {
    margin-top: 6px;
    font-weight: 300;
    font-size: 12px;
    letter-spacing: 0.12em;
    color: var(--ink-soft);
  }
  .contact-panel {
    position: absolute;
    left: 28px;
    right: 28px;
    top: 318px;
    height: 196px;
    background: var(--panel);
    padding: 34px 22px 0;
    font-family: "Nunito Sans", sans-serif;
    font-weight: 300;
    font-size: 12px;
    letter-spacing: 0.06em;
    line-height: 1.7;
    color: var(--ink);
  }
  .contact-row {
    display: flex;
    align-items: flex-start;
    gap: 10px;
    white-space: nowrap;
  }
  .contact-row svg {
    width: 11px;
    height: 11px;
    margin-top: 5px;
    flex: none;
  }
  .contact-row .no-icon { width: 11px; flex: none; }
  .tagline {
    position: absolute;
    left: 28px;
    bottom: 26px;
    font-family: "Nunito Sans", sans-serif;
    font-weight: 300;
    font-size: 10px;
    letter-spacing: 0.34em;
    color: var(--ink-soft);
    white-space: nowrap;
  }
</style>
</head>
<body>
<main class="stage">
  <section class="card card--front">
    <span class="brand-name">Harbor Lending Circle</span>
  </section>

  <section class="card card--back">
    <span class="brand-name">Harbor Lending Circle</span>

    <div class="holder">
      <p class="holder-name">Peter Wilks</p>
      <p class="holder-title">Co-Founder | Partner</p>
    </div>

    <div class="contact-panel">
      <div class="contact-row">
        <span class="no-icon"></span>
        <span>14 Cassia Lane, Suite 310</span>
      </div>
      <div class="contact-row">
        <svg viewBox="0 0 10 10" aria-hidden="true"><circle cx="5" cy="5" r="4.5" fill="var(--ink)"/><circle cx="5" cy="4.3" r="1.5" fill="var(--panel)"/></svg>
        <span>Singapore 047219</span>
      </div>
      <div class="contact-row">
        <svg viewBox="0 0 10 10" aria-hidden="true"><rect x="2.5" y="0.5" width="5" height="9" rx="1" fill="none" stroke="var(--ink)" stroke-width="1"/><line x1="4" y1="8" x2="6" y2="8" stroke="var(--ink)" stroke-width="0.8"/></svg>
        <span>+65 555-0142</span>
      </div>
      <div class="contact-row">
        <svg viewBox="0 0 10 10" aria-hidden="true"><rect x="0.5" y="2" width="9" height="6" fill="none" stroke="var(--ink)" stroke-width="1"/><polyline points="0.5,2 5,5.5 9.5,2" fill="none" stroke="var(--ink)" stroke-width="1"/></svg>
        <span>peterwilks@hlc-example.asia</span>
      </div>
      <div class="contact-row">
        <svg viewBox="0 0 10 10" aria-hidden="true"><circle cx="5" cy="5" r="4.3" fill="none" stroke="var(--ink)" stroke-width="1"/><ellipse cx="5" cy="5" rx="1.8" ry="4.3" fill="none" stroke="var(--ink)" stroke-width="0.8"/><line x1="0.7" y1="5" x2="9.3" y2="5" stroke="var(--ink)" stroke-width="0.8"/></svg>
        <span>www.hlc-example.asia</span>
      </div>
      <div class="contact-row">
        <span class="no-icon"></span>
        <span>WeChat: peterwilks</span>
      </div>
    </div>

    <p class="tagline">LENDING ACROSS SHORES</p>
  </section>
</main>
</body>
</html>
```